Labels for essential oils small botlles

We are Slovenia based company Velmora Tinctures Ltd. www.velmora-tinctures.example We offer essential oils as pure essential oils or blends (mixed) essential oils. We have different kind of essential oils 40+ and blends. We sell in different sizes as: 10ml, 30ml, 50ml and 100ml. But majority is 10ml.
All essential oils are in glass bottles with closer. We will now change bottles style from amber to cobalt blue with black closure (see picture attached)
We would like to have different stile of label for different category of essential oils. Here is link about different categories of essential oils https://www.quillbrookguides.example/mixing-tips/ . The different style / color could be by note:
- Top notes
- Middle notes
- Base notes
- Mixes – different oils mixed together and named as chill out, deep breath, sleep well, etc
Possible is also differentiation regarding:
• Citrus
• Floral
• Herbaceous
• Camphoraceous
• Spicy
• Resinous
• Woody
• Earthy
• Mixes

On labels should be also pictograms according to REACH directive of EU and label according to CPL (see attached file). We would also like to add EAN code attached on the edge of the label. On label is some text fixed I try to show in pdf attached file and some is variable depends from essential oil and date of production.

Meaning we need general labels for each note or other classification and one for mixes – you could also show your option or classification on something else with story behind.

10 ml roll 30 mm x 70 mm (1,25”x3”) but finial dimensions will follow.

We use Norvane Qt410 printer. For editing labels we use TagSmith which support also EAN codes. We import labels as picture in background or different according to your instructions.

Target Market(s)

Retail, health and wellness, all audiences and web shop

Industry/Entity Type

Health And Wellness

Font styles to use
Other font styles liked:
• GillLigHr is our font but could be different

Colors

Designer to choose colors to be used in the design.

Requirements
Must have
• Label should be as template that we could use for different oils in same group. More in attached document. According to CLP we have to put red pictograms on labels which is not nice and should be some how nicely integrated. on the edge EAB dar code that products could be sell through online.
Nice to have
• Different colours, some symbol as a drop or flower or herb. Logo is not necessary that is on label. We would like that label it self represent our brand.

```html
<!DOCTYPE html>
<html lang="en">
<head>
<meta charset="utf-8">
<title>Velmora Tinctures – Essential Oil Label, Herba No. 1</title>
<link rel="stylesheet" href="https://fonts.googleapis.com/css2?family=Playfair+Display:wght@700&family=Cormorant+Garamond:wght@500&family=Montserrat:wght@400&family=Barlow+Semi+Condensed:wght@300;700&display=swap">
<style>
  :root {
    --page-bg: #efefef;
    --label-black: #141414;
    --label-black-edge: #1f1f1f;
    --accent-green: #a6da57;
    --text-white: #f4f4f4;
    --text-black: #111111;
  }
  html, body {
    margin: 0;
    width: 1200px;
    height: 1200px;
    overflow: hidden;
    background: var(--page-bg);
  }
  .label {
    position: absolute;
    left: 237px;
    top: 138px;
    width: 726px;
    height: 924px;
    background: linear-gradient(90deg, var(--label-black-edge), var(--label-black) 30%, var(--label-black) 70%, var(--label-black-edge));
    color: var(--text-white);
  }
  .brand-frame {
    position: absolute;
    left: 35px;
    top: 4px;
    width: 627px;
    height: 167px;
    box-sizing: border-box;
    border: 6px solid var(--accent-green);
    border-top: none;
    display: flex;
    align-items: center;
    justify-content: center;
  }
  .brand-name {
    font-family: "Cormorant Garamond", serif;
    font-weight: 500;
    font-size: 42px;
    letter-spacing: 3px;
    text-transform: uppercase;
    white-space: nowrap;
    color: var(--text-white);
  }
  .category-title {
    position: absolute;
    left: 50px;
    top: 250px;
    margin: 0;
    writing-mode: vertical-rl;
    transform: rotate(180deg);
    white-space: nowrap;
    font-family: "Playfair Display", serif;
    font-weight: 700;
    font-size: 96px;
    line-height: 1;
    color: var(--text-white);
  }
  .purity {
    position: absolute;
    right: 103px;
    top: 256px;
    margin: 0;
    font-family: "Montserrat", sans-serif;
    font-weight: 400;
    font-size: 48px;
    line-height: 1;
    white-space: nowrap;
    color: var(--text-white);
  }
  .note-band {
    position: absolute;
    left: 202px;
    top: 337px;
    width: 418px;
    height: 85px;
    background: var(--accent-green);
    box-sizing: border-box;
    padding-right: 26px;
    display: flex;
    align-items: center;
    justify-content: flex-end;
    font-family: "Barlow Semi Condensed", sans-serif;
    font-weight: 700;
    font-size: 64px;
    line-height: 1;
    color: var(--text-black);
  }
  .ingredients {
    position: absolute;
    right: 130px;
    top: 448px;
    margin: 0;
    padding: 0;
    list-style: none;
    text-align: right;
    white-space: nowrap;
    font-family: "Barlow Semi Condensed", sans-serif;
    font-weight: 300;
    font-size: 46px;
    line-height: 64px;
    color: var(--text-white);
  }
  .blend-number {
    position: absolute;
    left: 528px;
    top: 739px;
    width: 88px;
    height: 88px;
    border-radius: 50%;
    background: var(--accent-green);
    display: flex;
    align-items: center;
    justify-content: center;
    font-family: "Barlow Semi Condensed", sans-serif;
    font-weight: 700;
    font-size: 64px;
    line-height: 1;
    color: var(--text-black);
  }
</style>
</head>
<body>
  <section class="label">
    <header class="brand-frame">
      <span class="brand-name">Velmora Tinctures</span>
    </header>
    <h1 class="category-title">Essential Oil</h1>
    <p class="purity">100% PURE</p>
    <div class="note-band">Herba</div>
    <ul class="ingredients">
      <li>Officinalis Oil</li>
      <li>Citrus Grandis Oil</li>
      <li>Mentha Viridis Oil</li>
    </ul>
    <div class="blend-number">1</div>
  </section>
</body>
</html>
```